Lívia Prado Arquitetura e Urbanismo precisa do Design de uma Página em Revista de Negócios

Preciso do design de uma página para publicar em uma revista de negócios, para Marketing, visando a expansão do meu serviço de Fortaleza para a região Centro-Sul do estado do Ceará. Trabalho com projetos de ambientação, bem como projeto arquitetônicos residenciais e comerciais. A página da revista tem dimensões de 21,5cm x 30,5cm e deve apresentar layout sofisticado e clean, usando tons de amarelo mostarda e branco, se assemelhando com a ideia da Revista Moradas (Fortaleza) e Lar Vivo. O projeto final deve comunicar sofisticação e confiança de que tenho a oferecer o que há de mais atual no mercado, trabalhando sempre a ideia da personalização.

```html
<!DOCTYPE html>
<html lang="pt-BR">
<head>
<meta charset="UTF-8">
<title>Lívia Prado Arquitetura e Urbanismo — Página de Revista</title>
<link href="https://fonts.googleapis.com/css2?family=Poppins:wght@600;700&family=Questrial&display=swap" rel="stylesheet">
<style>
  :root {
    --stage: #e9e6e1;
    --graphite: #414042;
    --ink: #050505;
    --mustard: #f2e51d;
    --white: #ffffff;
    --sketch-a: #4a4a4c;
    --sketch-b: #3a3a3c;
  }
  * { margin: 0; padding: 0; box-sizing: border-box; }
  html, body {
    width: 1200px; height: 1000px; overflow: hidden;
    background: var(--stage);
  }
  .page {
    position: absolute; left: 270px; top: 32px;
    width: 660px; height: 936px;
    background: var(--ink);
    overflow: hidden;
    box-shadow: 0 6px 24px rgba(0,0,0,.25);
  }
  .page__upper {
    position: absolute; left: 0; top: 0; width: 100%; height: 664px;
    background: var(--graphite);
  }
  .page__sketch {
    position: absolute; left: 0; top: 70px; width: 100%; height: 530px;
    background: linear-gradient(180deg, rgba(74,74,76,0) 0%, var(--sketch-a) 35%, var(--sketch-b) 85%, rgba(58,58,60,0) 100%);
  }
  .brand {
    position: absolute; left: 0; top: 150px; width: 100%;
    text-align: center;
    font-family: "Questrial", sans-serif;
    font-size: 22px; color: var(--mustard);
    letter-spacing: 1px;
  }
  .headline {
    position: absolute; left: 0; top: 230px; width: 100%;
    text-align: center;
  }
  .headline__light {
    display: block;
    font-family: "Questrial", sans-serif;
    font-size: 48px; line-height: 46px;
    color: var(--mustard);
    letter-spacing: -0.5px;
  }
  .headline__bold {
    display: block;
    font-family: "Poppins", sans-serif; font-weight: 600;
    font-size: 62px; line-height: 66px;
    color: var(--white);
    letter-spacing: -1.5px;
    margin-top: 8px;
  }
  .headline__bold + .headline__bold { margin-top: 0; }
  .gallery__item {
    position: absolute;
    border: 2px solid rgba(255,255,255,.85);
    box-shadow: 0 3px 10px rgba(0,0,0,.45);
  }
  .gallery__item--library { left: 30px;  top: 579px; width: 160px; height: 160px; background: linear-gradient(160deg, #e8b43a 0%, #d8d6d2 40%, #6b6e6a 100%); }
  .gallery__item--office  { left: 157px; top: 553px; width: 215px; height: 218px; background: linear-gradient(180deg, #bdbab5 0%, #e4e2de 55%, #d6b53c 100%); }
  .gallery__item--study   { left: 356px; top: 521px; width: 160px; height: 128px; background: linear-gradient(170deg, #e6e2da 0%, #3f8d88 60%, #c9a062 100%); }
  .gallery__item--garden  { left: 473px; top: 613px; width: 160px; height: 163px; background: linear-gradient(180deg, #7d9ac8 0%, #e9ebe8 40%, #3f6b2e 100%); }
  .gallery__item--bedroom { left: 321px; top: 648px; width: 160px; height: 160px; background: linear-gradient(180deg, #f1f0ee 0%, #2e3a55 50%, #d88a2a 100%); }
  .signature {
    position: absolute; left: 19px; top: 890px;
    font-size: 21px; color: var(--white);
    white-space: nowrap;
  }
  .signature__name {
    font-family: "Poppins", sans-serif; font-weight: 700;
    color: var(--mustard);
  }
  .signature__field {
    font-family: "Questrial", sans-serif;
    font-size: 16px;
    margin-left: 4px;
  }
</style>
</head>
<body>
  <article class="page">
    <div class="page__upper">
      <div class="page__sketch" role="img" aria-label="Desenho técnico em croqui de fachada e corte arquitetônico, em traço claro sobre fundo grafite"></div>
    </div>

    <div class="brand">Lívia Prado</div>

    <h1 class="headline">
      <span class="headline__light">projeto</span>
      <span class="headline__light">arquitetônicos</span>
      <span class="headline__bold">residenciais e</span>
      <span class="headline__bold">comerciais</span>
    </h1>

    <div class="gallery">
      <div class="gallery__item gallery__item--library" role="img" aria-label="Render de escritório com estante de livros e forro amarelo"></div>
      <div class="gallery__item gallery__item--office" role="img" aria-label="Render de sala de trabalho com mesa branca e cadeiras amarelas"></div>
      <div class="gallery__item gallery__item--study" role="img" aria-label="Render de quarto de estudos com marcenaria azul-petróleo"></div>
      <div class="gallery__item gallery__item--garden" role="img" aria-label="Render de fachada residencial com jardim e escada externa"></div>
      <div class="gallery__item gallery__item--bedroom" role="img" aria-label="Render de dormitório com cama e poltrona laranja"></div>
    </div>

    <p class="signature"><span class="signature__name">Lívia Prado</span><span class="signature__field">Arquitetura e Urbanismo</span></p>
  </article>
</body>
</html>
```